Dinewell - Slate App Design Project

I have a Slate app that serves as a restaurant reservation system. The design that i currently have is very basic apple design. I am looking for it to have a much more professional appeal.

Please review the attached document which contains all of the screen shots for the app.
Updates

This Project has now been Guaranteed.  I look forward to reviewing your designs.

Brent

Reason: I am extending my deadline because i just changed this contest to guaranteed and have received a ton more "acceptances" because of it and I want to give those designers a chance to submit a design.

Target Market(s)

restaurant owners

Industry/Entity Type

Restaurant

Requirements
Must have
• On the seating chart i am changing the feature that shows the tables highlighted and instead would like that replace with a badge. So the list of wait staff across the top of the seating chart would instead have a number next to their name and would correspond with the badge on the table to determine their section.

So for example:
Ada would have a number 1 in front of her name and tables 18, 19, 20, and 31 would have a little badge in the upper right hand corner with the number "1" inside the badge.
Uma would have a number 2 in front of her name and tables 6, 7, and 11 would have a little badge in the upper right hand corner with the number " 2" inside the badge.
Nora would have a number 3 in front of her name and tables 12, 13, 27, 28, 29, and 30 would have a little badge in the upper right hand corner with the number " 3" inside the badge.

The names on the top will all be ONE color

Also, i would like an icon developed to replace the "C" you see next to some of the people's name in the reservation and waitlist slots. Also, i would like a better looking "check mark".

```html
<!DOCTYPE html>
<html lang="en">
<head>
<meta charset="utf-8">
<title>Dinewell – Reservations</title>
<link href="https://fonts.googleapis.com/css2?family=Arimo:wght@400;700&display=swap" rel="stylesheet">
<style>
:root{
  --status-bg:#000;
  --cream:#fbf1d3;
  --cream-light:#fef8e6;
  --cream-line:#e9d7a6;
  --brown:#8b5716;
  --tab-top:#4aa7e2;
  --tab-bottom:#1c7bc2;
  --tab-active-top:#8cc6ea;
  --tab-active-bottom:#5aa9dc;
  --blue:#2a8ad4;
  --blue-badge:#2d93db;
  --gray-badge:#8d8d8d;
  --ink:#333;
  --panel-line:#d2d2d2;
  --full-bg:#e1f1fb;
  --floor-bg:#e4e4e4;
  --orange-note:#d97a10;
}
*{box-sizing:border-box;margin:0;padding:0}
html,body{width:1200px;height:901px;overflow:hidden}
body{font-family:"Arimo",Helvetica,Arial,sans-serif;background:var(--cream);position:relative;color:var(--ink)}

.status-bar{position:absolute;left:0;top:0;width:1200px;height:22px;background:var(--status-bg);color:#fff;font-size:15px;display:flex;align-items:center;justify-content:space-between;padding:0 10px}
.status-bar .clock{position:absolute;left:0;right:0;text-align:center;font-weight:700}

.top-bar{position:absolute;left:0;top:22px;width:1200px;height:51px;background:linear-gradient(#fdf6e2,#f6e8c2);border-bottom:1px solid var(--cream-line);display:flex;align-items:center;justify-content:space-between;padding:0 16px}
.brand{display:flex;align-items:center;gap:8px;color:var(--brown);font-size:24px}
.brand .mark{width:20px;height:20px;background:var(--brown);border-radius:3px;opacity:.75}
.stats{display:flex;gap:30px;align-items:center;color:var(--brown);font-size:22px;font-weight:700}
.stat{display:flex;align-items:center;gap:6px}
.stat svg{fill:var(--brown)}

.nav-bar{position:absolute;left:0;top:73px;width:1200px;height:65px;background:linear-gradient(#f3f3f3,#dcdcdc);border-bottom:1px solid #bdbdbd}
.tabs{position:absolute;left:361px;top:8px;width:832px;height:49px;display:flex;border-radius:7px;overflow:hidden;border:1px solid #1769a8}
.tab{flex:none;display:flex;align-items:center;justify-content:center;color:#fff;font-size:23px;background:linear-gradient(var(--tab-top),var(--tab-bottom));border-right:1px solid #1769a8}
.tab:last-child{border-right:0}
.tab.large{font-size:27px}
.tab.active{background:linear-gradient(var(--tab-active-top),var(--tab-active-bottom))}

.wait-list{position:absolute;left:0;top:138px;width:400px;height:763px;background:var(--cream-light);border-right:2px solid #cfc2a0}
.panel-head{height:51px;display:flex;align-items:center;justify-content:space-between;padding:0 16px 0 22px;font-size:23px;font-weight:700}
.wait-list .panel-head{color:var(--brown);background:linear-gradient(#fdf4d8,#f5e6bc);border-bottom:1px solid var(--cream-line)}
.plus{font-size:28px;font-weight:700;color:var(--brown)}
.guest{height:59px;display:flex;align-items:center;gap:8px;padding-left:12px;border-bottom:1px solid var(--cream-line);font-size:22px;font-weight:700;color:#3a3a3a}
.wait-badge,.party-badge{display:flex;align-items:center;gap:3px;height:25px;padding:0 6px;border-radius:6px;color:#fff;font-size:14px;font-weight:700}
.wait-badge{background:var(--blue-badge)}
.party-badge{background:var(--gray-badge)}
.guest .name{margin-left:4px;white-space:nowrap}

.floor{position:absolute;left:400px;top:138px;width:402px;height:763px;background:var(--floor-bg)}
.floor .panel-head{color:#444;background:linear-gradient(#f5f5f5,#dddddd);border-bottom:1px solid var(--panel-line);padding-left:22px}
.floor-plan{position:absolute;left:0;top:51px}

.schedule{position:absolute;left:802px;top:138px;width:398px;height:763px;background:#fff;border-left:1px solid #bdbdbd}
.slot{height:50px;display:flex;align-items:center;justify-content:space-between;padding:0 12px 0 22px;font-size:21px;font-weight:700;background:linear-gradient(#f5f5f5,#e6e6e6);border-bottom:1px solid var(--panel-line);color:#444}
.slot .open{display:flex;align-items:center;gap:14px}
.slot .add{color:#888;font-size:26px}
.slot.full{background:var(--full-bg);color:var(--blue)}
.slot.full .open{margin-right:70px}
.booking{padding:12px 22px 10px 14px;border-bottom:1px solid #e2e2e2;background:#f7fbfe;position:relative}
.booking .who{display:flex;align-items:center;gap:8px;font-size:21px;font-weight:700;color:#444}
.booking .note{font-size:17px;color:var(--blue);margin-top:8px;padding-left:4px}
.booking .note.warm{color:var(--orange-note);margin-top:4px}
.scroll-thumb{position:absolute;left:1181px;top:410px;width:4px;height:140px;border-radius:2px;background:var(--blue)}
</style>
</head>
<body>

<div class="status-bar">
  <span>Slate</span>
  <span class="clock">4:20 PM</span>
  <span>&#9679;</span>
</div>

<header class="top-bar">
  <div class="brand"><span class="mark"></span><span>Dinewell</span></div>
  <div class="stats">
    <div class="stat"><svg width="22" height="22" viewBox="0 0 22 22"><circle cx="11" cy="6" r="5"/><path d="M1 22c0-7 4-10 10-10s10 3 10 10z"/></svg>56</div>
    <div class="stat"><svg width="40" height="22" viewBox="0 0 40 22"><circle cx="9" cy="7" r="4"/><circle cx="31" cy="7" r="4"/><circle cx="20" cy="6" r="5"/><path d="M0 22c0-6 3-9 9-9s9 3 9 9zM22 22c0-6 3-9 9-9s9 3 9 9z"/><path d="M9 22c0-7 4-10 11-10s11 3 11 10z"/></svg>14</div>
    <div class="stat"><svg width="22" height="22" viewBox="0 0 22 22"><circle cx="11" cy="11" r="9" fill="none" stroke="#8b5716" stroke-width="2.5"/><path d="M11 5v6h5" fill="none" stroke="#8b5716" stroke-width="2.5"/></svg>25 m</div>
    <div class="stat"><svg width="26" height="22" viewBox="0 0 26 22"><rect x="1" y="3" width="24" height="5" rx="1"/><rect x="4" y="8" width="3" height="13"/><rect x="19" y="8" width="3" height="13"/></svg>11(296)</div>
    <div class="stat"><svg width="26" height="22" viewBox="0 0 26 22"><rect x="1" y="3" width="24" height="5" rx="1"/><rect x="4" y="8" width="3" height="13"/><rect x="19" y="8" width="3" height="13"/><rect x="11" y="8" width="3" height="13"/></svg>370</div>
  </div>
</header>

<nav class="nav-bar">
  <div class="tabs">
    <div class="tab" style="width:218px">Seating Chart</div>
    <div class="tab" style="width:128px">Specials</div>
    <div class="tab" style="width:148px">Staff Notes</div>
    <div class="tab large" style="width:152px">Calendar</div>
    <div class="tab large active" style="width:184px">Management</div>
  </div>
</nav>

<section class="wait-list">
  <div class="panel-head"><span>Wait List</span><span class="plus">+</span></div>
  <div class="guest"><span class="wait-badge">&#9719; 5</span><span class="party-badge">&#9679; 4</span><span class="name">Irene Calloway</span></div>
  <div class="guest"><span class="wait-badge">&#9719; 5</span><span class="party-badge">&#9679; 2</span><span class="name">Brent Sollis</span></div>
  <div class="guest"><span class="wait-badge">&#9719; 25</span><span class="party-badge">&#9679; 4</span><span class="name">Lena Fay</span></div>
  <div class="guest"><span class="wait-badge">&#9719; 25</span><span class="party-badge">&#9679; 3</span><span class="name">Oriel Banford</span></div>
  <div class="guest"><span class="wait-badge">&#9719; 30</span><span class="party-badge">&#9679; 4</span><span class="name">Marisol Quenbury</span></div>
  <div class="guest"><span class="wait-badge">&#9719; 30</span><span class="party-badge">&#9679; 6</span><span class="name">Tessa Morrow</span></div>
  <div class="guest"><span class="wait-badge">&#9719; 30</span><span class="party-badge">&#9679; 6</span><span class="name">Hattie Vale</span></div>
  <div class="guest"><span class="wait-badge">&#9719; 15</span><span class="party-badge">&#9679; 4</span><span class="name">Noreen Pellbrook</span></div>
  <div class="guest"><span class="wait-badge">&#9719; 40</span><span class="party-badge">&#9679; 5</span><span class="name">Miles Ardent</span></div>
</section>

<section class="floor">
  <div class="panel-head"><span>Floor Status</span><span style="color:#777;font-size:20px">&#9664;&#9654;</span></div>
  <svg class="floor-plan" width="402" height="712" viewBox="0 0 219 388" aria-label="Floor plan of tables">
    <defs>
      <linearGradient id="orange" x1="0" y1="0" x2="0" y2="1"><stop offset="0" stop-color="#d4892d"/><stop offset="1" stop-color="#a45d0f"/></linearGradient>
      <linearGradient id="gray" x1="0" y1="0" x2="0" y2="1"><stop offset="0" stop-color="#d2d2d2"/><stop offset="1" stop-color="#8f8f8f"/></linearGradient>
    </defs>
    <g fill="url(#orange)">
      <circle cx="18" cy="24" r="12"/><rect x="39" y="12" width="24" height="24" rx="2"/><rect x="186" y="12" width="24" height="24" rx="2"/>
      <circle cx="18" cy="57" r="12"/><rect x="39" y="45" width="24" height="24" rx="2"/>
      <rect x="78" y="44" width="10" height="34" rx="4"/><rect x="135" y="44" width="10" height="34" rx="4"/>
      <rect x="171" y="45" width="10" height="10" rx="2"/><rect x="187" y="45" width="10" height="10" rx="2"/>
      <rect x="171" y="61" width="10" height="10" rx="2"/><rect x="187" y="61" width="10" height="10" rx="2"/>
      <circle cx="18" cy="90" r="12"/><rect x="39" y="78" width="24" height="24" rx="2"/>
      <rect x="80" y="108" width="10" height="10" rx="2" transform="rotate(45 85 114)"/><rect x="100" y="108" width="10" height="10" rx="2" transform="rotate(45 105 114)"/>
      <circle cx="133" cy="96" r="7"/><circle cx="153" cy="96" r="7"/><circle cx="133" cy="114" r="7"/><circle cx="153" cy="114" r="7"/>
      <circle cx="18" cy="122" r="12"/>
      <rect x="79" y="134" width="33" height="10" rx="2"/><rect x="127" y="134" width="34" height="10" rx="2"/><rect x="177" y="134" width="33" height="10" rx="2"/>
      <rect x="80" y="156" width="10" height="10" rx="2" transform="rotate(45 85 161)"/><rect x="110" y="156" width="10" height="10" rx="2" transform="rotate(45 115 161)"/>
      <rect x="141" y="156" width="10" height="10" rx="2" transform="rotate(45 146 161)"/><rect x="172" y="156" width="10" height="10" rx="2" transform="rotate(45 177 161)"/>
    </g>
    <g fill="url(#gray)">
      <rect x="71" y="13" width="50" height="23" rx="3"/><rect x="129" y="13" width="50" height="23" rx="3"/>
      <rect x="107" y="44" width="10" height="34" rx="4"/>
      <rect x="80" y="90" width="10" height="10" rx="2" transform="rotate(45 85 96)"/><rect x="100" y="90" width="10" height="10" rx="2" transform="rotate(45 105 96)"/>
      <rect x="173" y="88" width="38" height="38" rx="3"/>
      <rect x="39" y="110" width="24" height="26" rx="2"/>
      <circle cx="18" cy="155" r="12"/><rect x="39" y="143" width="24" height="24" rx="2"/>
    </g>
  </svg>
</section>

<section class="schedule">
  <div class="slot"><span>12:00 PM</span><span class="open">Open 9(22) <span class="add">+</span></span></div>
  <div class="slot full"><span>12:15 PM</span><span class="open">Full</span></div>
  <div class="slot"><span>12:30 PM</span><span class="open">Open 12(20) <span class="add">+</span></span></div>
  <div class="slot"><span>12:45 PM</span><span class="open">Open&nbsp; 7(20) <span class="add">+</span></span></div>
  <div class="slot full"><span>1:00 PM</span><span class="open">Full</span></div>
  <div class="booking" style="height:102px">
    <div class="who"><span class="party-badge">&#9679; 2</span>Wren Talley</div>
    <div class="note">Quiet table in back</div>
    <div class="note warm">Prefers warm water...</div>
  </div>
  <div class="booking" style="height:58px">
    <div class="who"><span class="party-badge">&#9679; 4</span>Vesna Larkmoor</div>
  </div>
  <div class="booking" style="height:92px">
    <div class="who"><span class="party-badge">&#9679; 3</span>Corin Ashby</div>
    <div class="note">Booth Please</div>
  </div>
  <div class="booking" style="height:107px">
    <div class="who"><span class="party-badge">&#9679; 4</span>Della Orme</div>
  </div>
  <div class="slot"><span>1:15 PM</span><span class="open">17/20 <span class="add">+</span></span></div>
  <div class="slot full"><span>1:30 PM</span><span class="open">Full</span></div>
  <div class="slot"><span>1:45 PM</span><span class="open">4(20) <span class="add">+</span></span></div>
</section>
<div class="scroll-thumb"></div>

</body>
</html>
```